Real Estate Managemene Company Needs Business Card Design

We have a logo design and just need business cards made now for our business. Please use PDF logo # 3.

Card with Information to be attached shortly.

The card is used for a real estate management company. We will need to add four other employees and their cards.

Industry/Entity Type

Real Estate

Contact Information for Business Card

Tariq Hamdan
President
3187 Thornwick Avenue
Suite C
Maple Crossing, OH 44871
Phone 555.417.2286
Fax 555.417.2287
Cell 555.473.8062
vantorp@mailbreeze.net

Once design is approved we will have four other employees
Omar Hamdan
Operations Manager

Nadia Hamdan
Administrative Manager

Faz Hamdan
Principal

We would need to take out the cell # 555.473.8062 out for the remaining three cards.

Requirements
Must have
• Please use logo attached

```html
<!DOCTYPE html>
<html lang="en">
<head>
<meta charset="utf-8">
<title>Harborline Property Management Group – Business Card</title>
<link href="https://fonts.googleapis.com/css2?family=Source+Sans+3:wght@400;600;700&display=swap" rel="stylesheet">
<style>
  :root {
    --stage: #3b2c38;
    --card-white: #ffffff;
    --brand-blue: #0d5a8c;
    --ink: #1f1f21;
    --ink-soft: #3a3a3d;
  }
  * { box-sizing: border-box; margin: 0; padding: 0; }
  html, body {
    width: 1200px; height: 800px; overflow: hidden;
    background: var(--stage);
    font-family: "Source Sans 3", "Helvetica Neue", Arial, sans-serif;
  }
  .stage {
    width: 1200px; height: 800px;
    display: flex; flex-direction: column;
    align-items: center; justify-content: center; gap: 40px;
  }
  .card {
    position: relative;
    width: 560px; height: 320px;
    overflow: hidden;
    box-shadow: 0 10px 30px rgba(0,0,0,.35);
  }

  /* Front */
  .card-front { background: var(--card-white); color: var(--ink); }
  .skyline-fade {
    position: absolute; left: 120px; top: 0; width: 210px; height: 175px;
  }
  .holder { position: absolute; left: 34px; top: 40px; }
  .holder-name {
    font-size: 23px; font-weight: 700; color: var(--brand-blue); line-height: 1;
  }
  .holder-title { font-size: 13px; color: var(--ink-soft); margin-top: 4px; }
  .divider {
    position: absolute; left: 180px; top: 82px; width: 345px; height: 1.5px;
    background: var(--brand-blue);
  }
  .contact-list {
    position: absolute; left: 34px; top: 96px; list-style: none;
    font-size: 13.5px; color: var(--ink); line-height: 20px;
  }
  .contact-list li { display: flex; align-items: center; gap: 8px; }
  .contact-list svg { width: 11px; height: 11px; fill: var(--brand-blue); flex: none; }

  .brand-front {
    position: absolute; right: 34px; top: 26px;
    display: flex; align-items: center; gap: 10px;
  }
  .brand-mark-square { width: 14px; height: 14px; background: var(--brand-blue); flex: none; }
  .brand-name-front {
    font-size: 17px; font-weight: 600; color: var(--brand-blue);
    text-align: right; line-height: 1.15; letter-spacing: .3px;
  }

  .address {
    position: absolute; right: 34px; top: 190px;
    text-align: right; font-size: 14px; line-height: 19px; color: var(--ink);
    font-style: normal;
  }
  .footer-band { position: absolute; left: 0; bottom: 0; width: 560px; height: 44px; }

  /* Back */
  .card-back {
    background: var(--brand-blue);
    display: flex; align-items: center; justify-content: center; gap: 14px;
  }
  .brand-mark-square-back { width: 20px; height: 20px; background: #ffffff; flex: none; }
  .brand-name-back {
    color: #ffffff; font-size: 28px; font-weight: 600;
    line-height: 1.15; letter-spacing: .5px;
  }
</style>
</head>
<body>
<main class="stage">

  <section class="card card-front" aria-label="Business card front">
    <svg class="skyline-fade" role="img" aria-label="Faint skyline decoration" viewBox="0 0 210 175">
      <defs>
        <linearGradient id="fade" x1="0" y1="0" x2="0" y2="1">
          <stop offset="0" stop-color="#e4e6e9" stop-opacity=".9"/>
          <stop offset="1" stop-color="#ffffff" stop-opacity="0"/>
        </linearGradient>
      </defs>
      <rect width="210" height="175" fill="url(#fade)"/>
    </svg>

    <div class="holder">
      <p class="holder-name">Tariq Hamdan</p>
      <p class="holder-title">President</p>
    </div>
    <div class="divider"></div>

    <ul class="contact-list">
      <li>
        <svg viewBox="0 0 12 12" aria-hidden="true"><path d="M2.5 1h2l1 3-1.3 1a6 6 0 0 0 2.8 2.8l1-1.3 3 1v2a1.5 1.5 0 0 1-1.5 1.5A9.5 9.5 0 0 1 1 2.5 1.5 1.5 0 0 1 2.5 1z"/></svg>
        555.417.2286
      </li>
      <li>
        <svg viewBox="0 0 12 12" aria-hidden="true"><path d="M3 1h6v3H3zM1 5h10v5H9V8H3v2H1zM3.5 9h5v2h-5z"/></svg>
        555.417.2287
      </li>
      <li>
        <svg viewBox="0 0 12 12" aria-hidden="true"><path d="M3.5 0.5h5a1 1 0 0 1 1 1v9a1 1 0 0 1-1 1h-5a1 1 0 0 1-1-1v-9a1 1 0 0 1 1-1zM3.8 2v7h4.4V2z"/></svg>
        555.473.8062
      </li>
      <li>
        <svg viewBox="0 0 12 12" aria-hidden="true"><path d="M1 2.5h10v7H1zM1.8 3.3 6 6.5l4.2-3.2z" fill-rule="evenodd"/></svg>
        vantorp@mailbreeze.net
      </li>
    </ul>

    <div class="brand-front">
      <span class="brand-mark-square"></span>
      <p class="brand-name-front">Harborline Property<br>Management Group</p>
    </div>

    <address class="address">
      3187 Thornwick Avenue<br>
      Suite C<br>
      Maple Crossing, OH 44871
    </address>

    <svg class="footer-band" viewBox="0 0 560 44" preserveAspectRatio="none" aria-hidden="true">
      <polygon points="0,32 560,32 560,44 0,44" fill="var(--brand-blue)"/>
      <polygon points="310,22 560,22 560,44 290,44" fill="var(--ink)"/>
    </svg>
  </section>

  <section class="card card-back" aria-label="Business card back">
    <span class="brand-mark-square-back"></span>
    <p class="brand-name-back">Harborline Property<br>Management Group</p>
  </section>

</main>
</body>
</html>
```